Voyage Wellcare Hub Business Cards

We need business cards for our new start-up online travel health clinic. Visit our website voyagewellcarehub.ca for branding and more info.

Target Market(s)

Travellers

Industry/Entity Type

Business

Contact Information for Business Card

Maya Koslowski
maya@voyagewellcarehub.ca
+1 555 283 6194
voyagewellcarehub.ca

Font styles to use
Sans Serif

Colors
f68d4d

```html
<!DOCTYPE html>
<html lang="en">
<head>
<meta charset="utf-8">
<title>Voyage Wellcare Hub – Business Cards</title>
<link rel="stylesheet" href="https://fonts.googleapis.com/css2?family=Open+Sans:wght@400;600;700&display=swap">
<style>
  :root {
    --brand-orange: #f68d4d;
    --band-orange: #e98a47;
    --ink-gray: #8a8a8a;
    --soft-gray: #c4c4c4;
    --light-gray: #e2e2e2;
    --card-white: #ffffff;
    --backdrop: #dfe1df;
  }
  html, body {
    margin: 0;
    width: 1200px;
    height: 900px;
    overflow: hidden;
    background: var(--backdrop);
    font-family: "Open Sans", Arial, sans-serif;
  }
  .stage {
    position: relative;
    width: 1200px;
    height: 900px;
  }
  .card {
    position: absolute;
    width: 520px;
    height: 297px;
    box-shadow: 0 6px 18px rgba(0,0,0,0.25);
  }
  .card svg { display: block; width: 100%; height: 100%; }
  .card--front { left: 150px; top: 150px; }
  .card--back { left: 530px; top: 455px; }

  .wordmark { font-family: "Open Sans", Arial, sans-serif; font-weight: 400; fill: var(--brand-orange); }
  .wordmark--light { fill: var(--card-white); }
  .tagline { font-family: "Open Sans", Arial, sans-serif; font-weight: 400; fill: var(--ink-gray); }
  .tagline--light { fill: #fde3d2; }
  .person-name { font-family: "Open Sans", Arial, sans-serif; font-weight: 700; fill: var(--brand-orange); letter-spacing: -0.3px; }
  .contact-line { font-family: "Open Sans", Arial, sans-serif; font-weight: 400; fill: var(--brand-orange); }
  .contact-icon { fill: var(--ink-gray); }
</style>
</head>
<body>
<main class="stage">

  <section class="card card--front" aria-label="Business card front">
    <svg viewBox="0 0 520 297" xmlns="http://www.w3.org/2000/svg">
      <defs>
        <linearGradient id="front-paper" x1="0" y1="0" x2="1" y2="1">
          <stop offset="0" stop-color="#ffffff"/>
          <stop offset="1" stop-color="#ececec"/>
        </linearGradient>
        <linearGradient id="gray-swoosh" x1="0" y1="0" x2="1" y2="0">
          <stop offset="0" stop-color="#f1f1f1"/>
          <stop offset="0.6" stop-color="#c9c9c9"/>
          <stop offset="1" stop-color="#a9a9a9"/>
        </linearGradient>
      </defs>
      <rect class="card-paper" width="520" height="297" fill="url(#front-paper)"/>
      <path class="swoosh swoosh--gray" d="M0,232 C160,222 380,196 520,118 L520,170 C400,210 200,230 0,244 Z" fill="url(#gray-swoosh)"/>
      <path class="swoosh swoosh--orange" d="M0,222 C140,230 320,212 480,180 C330,222 160,246 0,252 Z" fill="var(--band-orange)"/>
      <text class="wordmark" x="68" y="142" font-size="31">Voyage Wellcare Hub</text>
      <text class="tagline" x="196" y="162" font-size="11.5">Online Travel Health Experts</text>
    </svg>
  </section>

  <section class="card card--back" aria-label="Business card back">
    <svg viewBox="0 0 520 297" xmlns="http://www.w3.org/2000/svg">
      <defs>
        <linearGradient id="back-paper" x1="0" y1="0" x2="1" y2="1">
          <stop offset="0" stop-color="#f6f6f6"/>
          <stop offset="1" stop-color="#ffffff"/>
        </linearGradient>
      </defs>
      <rect class="card-paper" width="520" height="297" fill="url(#back-paper)"/>
      <path class="panel-edge panel-edge--gray" d="M272,0 H300 C325,40 338,90 322,140 C306,195 318,240 336,297 H318 C296,240 288,195 304,140 C318,90 305,40 272,0 Z" fill="var(--soft-gray)"/>
      <path class="panel-edge panel-edge--white" d="M286,0 H300 C325,40 338,90 322,140 C306,195 318,240 336,297 H328 C308,240 300,195 314,140 C328,90 318,40 286,0 Z" fill="var(--light-gray)"/>
      <path class="brand-panel" d="M300,0 H520 V297 H336 C318,240 306,195 322,140 C338,90 325,40 300,0 Z" fill="var(--brand-orange)"/>

      <text class="person-name" x="48" y="142" font-size="24">MAYA KOSLOWSKI</text>
      <line class="name-rule" x1="48" y1="156" x2="168" y2="156" stroke="var(--soft-gray)" stroke-width="1.5"/>

      <g class="contact-list">
        <circle class="contact-icon" cx="56" cy="222" r="3.5" fill="none" stroke="var(--ink-gray)" stroke-width="1.3"/>
        <text class="contact-line" x="68" y="226" font-size="11.5">maya@voyagewellcarehub.ca</text>

        <path class="contact-icon" d="M53,237 l3,-1 2,3 -1.5,1.5 c1,2 2,3 3.5,3.5 l1.5,-1.5 3,2 -1,3 c-5,0 -10.5,-5 -10.5,-10.5 Z"/>
        <text class="contact-line" x="68" y="246" font-size="11.5">+1 555 283 6194</text>

        <path class="contact-icon" d="M56,256 l-5,4.5 h1.5 v4.5 h2.5 v-3 h2 v3 h2.5 v-4.5 h1.5 Z"/>
        <text class="contact-line" x="68" y="266" font-size="11.5">voyagewellcarehub.ca</text>
      </g>

      <text class="wordmark wordmark--light" x="342" y="188" font-size="16.5">Voyage Wellcare Hub</text>
      <text class="tagline tagline--light" x="388" y="199" font-size="7">Online Travel Health Experts</text>
    </svg>
  </section>

</main>
</body>
</html>
```